Surgery Office Letterhead Design

I'm seeking new letterhead that will comprise all of our office locations and logo and other applicable information, per the following:

Office Locations:

Bluewater Institute for Oral & Facial Surgery at Marlowe
347 Amberly Lane
Marlowe, Texas 75058
Phone 555.392.4806
Fax 555.392.7734

Bluewater Institute for Oral & Facial Surgery at Ashbrook Falls
588 Quarry Hollow Parkway
Ashbrook Falls, Texas 75428
Phone 555.763.2248
Fax 555.763.2251

Bluewater Institute for Oral & Facial Surgery at Kestra
715 West 9th Street
Kestra, Texas 75537
Phone 555.481.6072
Fax 555.481.6079

Other Info to include:

www.bluewatermaxillo.example
hello@bluewatermaxillo.example

Industry/Entity Type

Medical

Font styles to use
Serif
Sans Serif

Requirements
Must have
• See Project Description

```html
<!DOCTYPE html>
<html lang="en">
<head>
<meta charset="utf-8">
<title>Bluewater Institute for Oral &amp; Facial Surgery — Letterhead</title>
<link rel="stylesheet" href="https://fonts.googleapis.com/css2?family=Arimo&family=Cinzel:wght@500&display=swap">
<style>
  :root {
    --paper: #ffffff;
    --sidebar: #ff80ff;
    --band: #ffe6fb;
    --ink-name: #111122;
    --ink-contact: #ffffff;
  }
  * { margin: 0; padding: 0; box-sizing: border-box; }
  html, body { width: 927px; height: 1200px; overflow: hidden; background: var(--paper); }
  .letterhead { position: relative; width: 927px; height: 1200px; background: var(--paper); }
  .brand-name {
    position: absolute; left: 74px; top: 96px;
    font-family: "Cinzel", serif; font-weight: 500; color: var(--ink-name);
    line-height: 1;
  }
  .brand-name .primary { display: block; font-size: 21px; letter-spacing: 0.2px; }
  .brand-name .secondary { display: block; font-size: 10.5px; margin-top: 4px; letter-spacing: 0.3px; }
  .header-band {
    position: absolute; left: 0; top: 137px; width: 686px; height: 17px;
    background: var(--band);
  }
  .contact-column {
    position: absolute; left: 686px; top: 0; width: 241px; height: 1200px;
    background: var(--sidebar);
    font-family: "Arimo", sans-serif; color: var(--ink-contact);
    font-size: 11.6px; line-height: 14.5px;
  }
  .office { position: absolute; left: 36px; width: 200px; font-style: normal; }
  .office-name { margin-bottom: 4px; }
  .office--north { top: 89px; }
  .office--west { top: 189px; }
  .office--south { top: 290px; }
  .online { position: absolute; left: 36px; top: 397px; }
</style>
</head>
<body>
<div class="letterhead">
  <div class="brand-name">
    <span class="primary">BLUEWATER INSTITUTE</span>
    <span class="secondary">FOR ORAL &amp; FACIAL SURGERY</span>
  </div>
  <div class="header-band"></div>

  <aside class="contact-column">
    <address class="office office--north">
      <p class="office-name">Bluewater Institute for Oral &amp; Facial Surgery at Marlowe</p>
      <p>347 Amberly Lane<br>Marlowe, Texas 75058<br>Phone 555.392.4806<br>Fax 555.392.7734</p>
    </address>
    <address class="office office--west">
      <p class="office-name">Bluewater Institute for Oral &amp; Facial Surgery at Ashbrook Falls</p>
      <p>588 Quarry Hollow Parkway<br>Ashbrook Falls, Texas 75428<br>Phone 555.763.2248<br>Fax 555.763.2251</p>
    </address>
    <address class="office office--south">
      <p class="office-name">Bluewater Institute for Oral &amp; Facial Surgery at Kestra</p>
      <p>715 West 9th Street<br>Kestra, Texas 75537<br>Phone 555.481.6072<br>Fax 555.481.6079</p>
    </address>
    <p class="online">www.bluewatermaxillo.example<br>hello@bluewatermaxillo.example</p>
  </aside>
</div>
</body>
</html>
```